Life Coach for Lawyers Business Card Design

Elegant, original, business card design for life coaching service for associate attorneys who work in big law and struggle with stress, overwhelm, and time management. Double sided design.

Target Market(s)

Women associate attorneys who work in big law and struggle with stress, overwhelm, and time management.

Industry/Entity Type

Life Coaching

Contact Information for Business Card

Marissa Pendrell
Life Coach
518.677.3941
calmbriefcounsel.net
marissa@calmbriefcounsel.net
@calmbriefcounsel (Instagram)

Font styles to use
Other font styles liked:
• Silver South font duo. See uploaded files.

Requirements
Must have
• Icons for phone, website, email, and Instagram instead of words. Specific colors used in my logo (171B2B, 421121, FFFFFF)
Nice to have
• Foil. Embossed. Feminine design.
Should not have
• Any colors other than those used in logo. See uploaded files.

```html
<!DOCTYPE html>
<html lang="en">
<head>
<meta charset="utf-8">
<title>Calm Brief Counsel — Business Card</title>
<link rel="stylesheet" href="https://fonts.googleapis.com/css2?family=Bodoni+Moda:wght@400;500&family=Mr+Dafoe&display=swap">
<style>
  :root {
    --navy: #171B2B;
    --wine: #421121;
    --white: #FFFFFF;
    --stage: #E8E6EA;
  }
  * { box-sizing: border-box; margin: 0; padding: 0; }
  html, body {
    width: 1200px; height: 1200px; overflow: hidden;
    background: var(--stage);
  }
  .sheet { position: relative; width: 1200px; height: 1200px; }

  .card {
    position: absolute; left: 243px;
    width: 715px; overflow: hidden;
  }
  .card-front {
    top: 197px; height: 373px;
    background: var(--white);
    border-radius: 58px;
  }
  .card-back {
    top: 621px; height: 381px;
    background: var(--navy);
  }
  .card-bands { position: absolute; left: 0; bottom: 0; display: block; }

  .brand-name {
    position: absolute; left: 78px; top: 86px;
    font-family: "Bodoni Moda", serif; font-weight: 400;
    font-size: 23px; letter-spacing: 1.5px; line-height: 1.12;
    color: var(--wine); text-transform: uppercase;
  }

  .person { position: absolute; right: 90px; top: 76px; text-align: right; }
  .person-name {
    font-family: "Mr Dafoe", cursive; font-size: 30px;
    color: var(--wine); line-height: 1.1; white-space: nowrap;
  }
  .person-title {
    font-family: "Bodoni Moda", serif; font-size: 20px;
    color: var(--navy); letter-spacing: 1.5px; margin-top: 6px;
  }

  .contact-list {
    position: absolute; left: 77px; top: 192px; list-style: none;
  }
  .contact-item {
    display: flex; align-items: center; height: 25.5px;
    font-family: "Bodoni Moda", serif; font-size: 15px;
    color: var(--navy); letter-spacing: 0.6px; text-transform: uppercase;
  }
  .contact-icon { width: 20px; height: 20px; margin-right: 11px; flex: none; }

  .back-brand {
    position: absolute; left: 0; right: 0; top: 138px;
    text-align: center;
    font-family: "Bodoni Moda", serif; font-weight: 400;
    font-size: 44px; letter-spacing: 3px; line-height: 1.1;
    color: var(--white); text-transform: uppercase;
  }
</style>
</head>
<body>
<main class="sheet">

  <section class="card card-front" aria-label="Card front">
    <div class="brand-name">Calm Brief<br>Counsel</div>

    <div class="person">
      <div class="person-name">Marissa Pendrell</div>
      <div class="person-title">LIFE COACH</div>
    </div>

    <ul class="contact-list">
      <li class="contact-item">
        <svg class="contact-icon" viewBox="0 0 20 20" aria-hidden="true">
          <circle cx="10" cy="10" r="9" fill="none" stroke="#421121" stroke-width="1.4"/>
          <path d="M7 5.5c-.8.4-1.5 1.2-1.2 2.4.7 2.8 3.1 5.4 5.9 6.3 1.2.4 2-.3 2.5-1.1l-1.8-1.4-1 .7c-1.3-.6-2.4-1.8-3-3.1l.8-.9z" fill="#421121"/>
        </svg>
        518.677.3941
      </li>
      <li class="contact-item">
        <svg class="contact-icon" viewBox="0 0 20 20" aria-hidden="true">
          <circle cx="10" cy="10" r="9" fill="none" stroke="#421121" stroke-width="1.4"/>
          <circle cx="10" cy="10" r="5" fill="none" stroke="#421121" stroke-width="1.2"/>
          <path d="M5 10h10M10 5c-2 2.8-2 7.2 0 10M10 5c2 2.8 2 7.2 0 10" fill="none" stroke="#421121" stroke-width="1"/>
        </svg>
        calmbriefcounsel.net
      </li>
      <li class="contact-item">
        <svg class="contact-icon" viewBox="0 0 20 20" aria-hidden="true">
          <circle cx="10" cy="10" r="9" fill="none" stroke="#421121" stroke-width="1.4"/>
          <rect x="5" y="7" width="10" height="7" rx="1" fill="#421121"/>
          <path d="M5.5 7.5l4.5 3.5 4.5-3.5" fill="none" stroke="#FFFFFF" stroke-width="1"/>
        </svg>
        marissa@calmbriefcounsel.net
      </li>
      <li class="contact-item">
        <svg class="contact-icon" viewBox="0 0 20 20" aria-hidden="true">
          <circle cx="10" cy="10" r="9" fill="none" stroke="#421121" stroke-width="1.4"/>
          <circle cx="10" cy="10" r="3.2" fill="#421121"/>
        </svg>
        @calmbriefcounsel
      </li>
    </ul>

    <svg class="card-bands" width="715" height="20" viewBox="0 0 715 20" aria-hidden="true">
      <polygon points="0,0 325,0 357,20 0,20" fill="#421121"/>
      <polygon points="379,0 715,0 715,20 409,20" fill="#171B2B"/>
    </svg>
  </section>

  <section class="card card-back" aria-label="Card back">
    <div class="back-brand">Calm Brief<br>Counsel</div>

    <svg class="card-bands" width="715" height="19" viewBox="0 0 715 19" aria-hidden="true">
      <polygon points="0,0 315,0 345,19 0,19" fill="#421121"/>
      <polygon points="368,0 715,0 715,19 399,19" fill="#FFFFFF"/>
    </svg>
  </section>

</main>
</body>
</html>
```